Business Card Design Project

This is the first time we use our new logo. We need a business card that we can use both on our institutional corporate relationships and also that works for our staff that deals with consumers directly.

VELUNDA is a new company dedicated to empower consumers and to provide them with the best choices for specialized health care using the latest telemedicine technology (medicine at a distance via videoconference).

We want to print this cards in high quality materials and process. We will like designs that allow us to use UV spot varnish and other techniques that will differentiate us.

We are including Two different versions of Color logos. In addition we are including white over black background logos. Those can be used replacing the black for a color.

Please note this is the first time we will be creating any corporate materials with our new logo and colors.

Target Market(s)

34+ consumers of medium high and high socioeconomic levels.

Industry/Entity Type

Health

Requirements
Must have
• Our logo on its original colors
Should not have
• Any other graphical element or design that is not our logo

```html
<!DOCTYPE html>
<html lang="en">
<head>
<meta charset="utf-8">
<title>VELUNDA Business Card</title>
<link rel="stylesheet" href="https://fonts.googleapis.com/css2?family=Open+Sans:wght@400;600;700&display=swap">
<style>
  :root {
    --page-bg: #ffffff;
    --card-dark: #0d0d0d;
    --card-light: #ffffff;
    --ink-light: #ffffff;
    --ink-dark: #111111;
    --emboss: #e6e6e6;
    --emboss-edge: #cfcfcf;
    --dash: #c8c8c8;
  }
  html, body {
    margin: 0;
    padding: 0;
    width: 912px;
    height: 1200px;
    overflow: hidden;
    background: var(--page-bg);
    font-family: "Open Sans", Arial, sans-serif;
  }
  .canvas {
    position: relative;
    width: 912px;
    height: 1200px;
  }
  .card {
    position: absolute;
    box-sizing: border-box;
  }
  .card--front {
    left: 81px;
    top: 58px;
    width: 760px;
    height: 492px;
    background: var(--card-dark);
  }
  .card--back {
    left: 77px;
    top: 638px;
    width: 764px;
    height: 494px;
    background: var(--card-light);
    border: 1.5px dashed var(--dash);
  }
  .brand-mark {
    position: absolute;
    left: 50%;
    transform: translateX(-50%);
    border-radius: 50%;
  }
  .card--front .brand-mark {
    top: 110px;
    width: 120px;
    height: 120px;
    background: var(--ink-light);
  }
  .brand-name {
    position: absolute;
    left: 0;
    right: 0;
    margin: 0;
    text-align: center;
    font-weight: 700;
    letter-spacing: 6px;
    line-height: 1;
  }
  .card--front .brand-name {
    top: 350px;
    font-size: 72px;
    color: var(--ink-light);
  }
  .card--back .brand-mark {
    top: 90px;
    width: 150px;
    height: 150px;
    background: var(--emboss);
  }
  .card--back .brand-name {
    top: 262px;
    font-size: 30px;
    letter-spacing: 4px;
    color: var(--emboss-edge);
  }
  .contact {
    position: absolute;
    left: 0;
    right: 0;
    top: 350px;
    color: var(--ink-dark);
    font-size: 25px;
    line-height: 1;
  }
  .contact__address {
    margin: 0;
    text-align: center;
  }
  .contact__grid {
    display: grid;
    grid-template-columns: auto auto;
    column-gap: 26px;
    row-gap: 11px;
    justify-content: center;
    margin-top: 16px;
  }
</style>
</head>
<body>
  <main class="canvas">
    <section class="card card--front" aria-label="Card front">
      <div class="brand-mark"></div>
      <h1 class="brand-name">VELUNDA</h1>
    </section>

    <section class="card card--back" aria-label="Card back">
      <div class="brand-mark"></div>
      <p class="brand-name">VELUNDA</p>
      <div class="contact">
        <p class="contact__address">ADRESS | ADRESS | ADRESS | ADRESS</p>
        <div class="contact__grid">
          <span class="contact__phone">PH: 000 000 0000</span>
          <span class="contact__email">info@velunda.com</span>
          <span class="contact__fax">FX: 000 000 0000</span>
          <span class="contact__web">www.velunda.com</span>
        </div>
      </div>
    </section>
  </main>
</body>
</html>
```